Skills training in Materials Stewardship

Need design of a business card (later to be completed by letterhead and webdesign in same fashion) for a professional who works in the field of capacity building of professionals in mostly developing countries in the field waste/resource management, waste prevention/reduction, cleaner production, stakeholders involvement, etc.
Info on business cards is to include provided logo, info in provided file and picture.

Industry/Entity Type

Business

Contact Information for Business Card

White background

Font styles to use
Sans Serif

Colors

Designer to choose colors to be used in the design.

```html
<!DOCTYPE html>
<html lang="en">
<head>
<meta charset="utf-8">
<title>Terra-Learn Business Card</title>
<link rel="stylesheet" href="https://fonts.googleapis.com/css2?family=Open+Sans:wght@400;600;700&display=swap">
<style>
  :root {
    --page-bg: #e9e7e3;
    --card-bg: #ffffff;
    --brand-green: #4c9a3c;
    --text-dark: #2f2f2f;
    --photo-top: #9fb58c;
    --photo-mid: #c9b59f;
    --photo-low: #e6e3dc;
  }
  * { margin: 0; padding: 0; box-sizing: border-box; }
  html, body {
    width: 1200px; height: 1047px; overflow: hidden;
    background: var(--page-bg);
    font-family: "Open Sans", sans-serif;
  }
  .card {
    position: absolute; left: 100px; top: 249px;
    width: 1000px; height: 549px;
    background: var(--card-bg);
    border-radius: 22px; overflow: hidden;
    box-shadow: 0 6px 24px rgba(0,0,0,0.12);
  }
  .portrait {
    position: absolute; left: 0; top: 0; width: 455px; height: 100%;
    background: linear-gradient(160deg, var(--photo-top) 0%, #8aa27a 35%, var(--photo-mid) 60%, var(--photo-low) 100%);
  }
  .divider {
    position: absolute; left: 455px; top: 0; width: 5px; height: 100%;
    background: var(--brand-green);
  }
  .logo {
    position: absolute; left: 497px; top: 52px;
    display: flex; align-items: center; gap: 14px;
  }
  .logo-mark { width: 44px; height: 44px; background: var(--brand-green); }
  .logo-name {
    font-size: 46px; font-weight: 700; color: var(--brand-green);
    line-height: 1; letter-spacing: 0.5px;
  }
  .company {
    position: absolute; left: 495px; top: 168px;
    font-size: 41px; font-weight: 600; color: var(--brand-green); line-height: 1.1;
  }
  .tagline {
    position: absolute; left: 495px; top: 216px;
    font-size: 21px; color: var(--text-dark); line-height: 30px;
  }
  .rule {
    position: absolute; left: 495px; width: 505px; height: 2px;
    background: var(--brand-green);
  }
  .rule-upper { top: 288px; }
  .rule-lower { top: 410px; }
  .address {
    position: absolute; left: 495px; top: 331px;
    font-size: 21px; color: var(--text-dark); line-height: 30px;
  }
  .social {
    position: absolute; left: 783px; top: 301px;
    list-style: none; font-size: 21px; color: var(--text-dark); line-height: 30px;
  }
  .social li { display: flex; align-items: center; gap: 12px; }
  .social-dot { width: 14px; height: 14px; background: var(--brand-green); border-radius: 3px; }
  .contact {
    position: absolute; left: 497px; top: 428px;
    list-style: none; font-size: 21px; color: var(--text-dark); line-height: 31px;
    letter-spacing: 0.4px;
  }
  .contact li { display: flex; align-items: center; gap: 13px; }
  .contact svg { width: 16px; height: 16px; flex: none; }
</style>
</head>
<body>
  <div class="card">
    <div class="portrait" role="img" aria-label="Portrait photo of the consultant in a white shirt, outdoors in front of greenery"></div>
    <div class="divider"></div>

    <div class="logo">
      <span class="logo-mark"></span>
      <span class="logo-name">terra-learn</span>
    </div>

    <div class="company">Terra-Learn</div>
    <div class="tagline">Skills training in<br>Materials Stewardship</div>

    <div class="rule rule-upper"></div>

    <div class="address">Kastanienweg 18<br>10437 Berlin Germany</div>

    <ul class="social">
      <li><span class="social-dot"></span>@jonasvelder</li>
      <li><span class="social-dot"></span>velder2010</li>
      <li><span class="social-dot"></span>Jonas Velder</li>
    </ul>

    <div class="rule rule-lower"></div>

    <ul class="contact">
      <li>
        <svg viewBox="0 0 16 16"><path d="M3.5 1.5l3 3-1.6 1.8c.9 2 2.4 3.5 4.4 4.4l1.8-1.6 3 3-1.7 1.9C7.5 14 2 8.5 1.6 3.2z" fill="var(--brand-green)"/></svg>
        +49 1500 000 1234 (also mobile)
      </li>
      <li>
        <svg viewBox="0 0 16 16"><rect x="1.5" y="3.5" width="13" height="9" fill="none" stroke="var(--brand-green)" stroke-width="1.5"/><path d="M1.5 3.5l6.5 5 6.5-5" fill="none" stroke="var(--brand-green)" stroke-width="1.5"/></svg>
        jonas.velder@terra-learn.com
      </li>
      <li>
        <svg viewBox="0 0 16 16"><circle cx="8" cy="8" r="6.5" fill="none" stroke="var(--brand-green)" stroke-width="1.4"/><ellipse cx="8" cy="8" rx="2.8" ry="6.5" fill="none" stroke="var(--brand-green)" stroke-width="1.2"/><path d="M1.5 8h13" stroke="var(--brand-green)" stroke-width="1.2"/></svg>
        www.terra-learn.com
      </li>
    </ul>
  </div>
</body>
</html>
```